I need to redesign this website. Modern Fun Professional Redesign For www.JollyPerkHub.com = New Name www.ClaimVouchly.com

Use existing content as it is on website exactly and we will revise after initial mock ups.

The new name will be ClaimVouchly.com please make a quick logo for this site too while redesigning.

Make it look like an official website....

Target Market(s)

Consumers that are redeeming certificates that businesses gave to them as a gift for customer loyalty,e tc.

Industry/Entity Type

It Professional

Logo Text

www.ClaimVouchly.com

Number of Pages Required

4 page

Colors

Designer to choose colors to be used in the design.

Requirements
Must have
• Must look professional, build trust and credibility.
Nice to have
• open
Should not have
• open

```html
<!DOCTYPE html>
<html lang="en">
<head>
<meta charset="UTF-8">
<title>ClaimVouchly.com – The Redemption Source</title>
<link href="https://fonts.googleapis.com/css2?family=Montserrat:wght@400;500;600;700;800&display=swap" rel="stylesheet">
<style>
  :root {
    --green: #2fd12a;
    --ink: #1c1c1c;
    --text: #2a2a2a;
    --muted: #6a6a6a;
    --light: #efefef;
    --white: #ffffff;
    --footer: #1f2022;
    --divider: #555555;
    --hero-a: #2a3138;
    --hero-b: #4b565f;
    --hero-c: #11161b;
    --social-1: #3b5b9a;
    --social-2: #1d78b3;
    --social-3: #d23a2a;
  }
  * { box-sizing: border-box; margin: 0; padding: 0; }
  html, body { width: 720px; height: 1200px; overflow: hidden; background: var(--white); }
  body { font-family: "Montserrat", Arial, sans-serif; color: var(--text); text-transform: uppercase; }
  .page { position: relative; width: 720px; height: 1200px; overflow: hidden; }

  /* Hero */
  .hero { position: relative; height: 450px; color: var(--white); }
  .hero-photo { position: absolute; inset: 0; background: linear-gradient(120deg, var(--hero-a) 0%, var(--hero-b) 45%, var(--hero-c) 100%); }
  .hero-shade { position: absolute; inset: 0; background: rgba(0,0,0,0.35); }
  .hero-inner { position: relative; height: 100%; }
  .brand { position: absolute; left: 20px; top: 26px; font-weight: 700; font-size: 17px; color: var(--white); text-transform: none; }
  .nav { position: absolute; right: 20px; top: 28px; display: flex; gap: 16px; }
  .nav a { color: var(--white); text-decoration: none; font-size: 14px; font-weight: 500; }
  .nav a.active { color: var(--green); }
  .hero-title { position: absolute; top: 118px; width: 100%; text-align: center; font-size: 30px; font-weight: 700; letter-spacing: 0.5px; }
  .hero-sub { position: absolute; top: 160px; width: 100%; text-align: center; font-size: 14px; font-weight: 600; }
  .redeem-form { position: absolute; top: 196px; left: 72px; width: 558px; height: 50px; display: flex; }
  .redeem-input { flex: 1; background: rgba(0,0,0,0.55); border-bottom: 2px solid var(--green); color: var(--white); font-size: 12px; font-weight: 600; padding: 17px 16px; }
  .redeem-go { width: 120px; background: var(--green); color: var(--white); font-size: 26px; font-weight: 700; display: flex; align-items: center; justify-content: center; }
  .hero-note { position: absolute; top: 266px; width: 100%; text-align: center; font-size: 12px; font-weight: 500; }

  /* Sections */
  .section-title { text-align: center; font-size: 20px; font-weight: 700; color: var(--ink); }
  .section-title::after { content: ""; display: block; width: 40px; height: 4px; background: var(--green); margin: 5px auto 0; }

  .about { height: 143px; background: var(--light); padding: 8px 24px 0; }
  .about p { font-size: 9px; font-weight: 600; line-height: 1.4; color: var(--text); margin-top: 9px; }

  .testimonials { height: 295px; background: var(--white); padding-top: 32px; text-align: center; }
  .quote { width: 660px; margin: 36px auto 0; font-size: 16px; font-weight: 500; line-height: 1.9; color: var(--ink); }
  .author { margin-top: 4px; font-size: 20px; font-weight: 700; color: var(--ink); }
  .author::after { content: ""; display: block; width: 40px; height: 4px; background: var(--green); margin: 3px auto 0; }
  .arrows { margin-top: 22px; display: flex; justify-content: center; gap: 10px; }

  .newsletter { height: 125px; background: var(--light); padding-top: 24px; }
  .newsletter-form { width: 270px; height: 26px; margin: 16px auto 0; display: flex; }
  .newsletter-input { flex: 1; background: var(--white); border-bottom: 2px solid var(--green); font-size: 9px; padding: 8px; color: var(--muted); }
  .newsletter-send { width: 68px; background: var(--green); color: var(--white); font-weight: 700; font-size: 13px; display: flex; align-items: center; justify-content: center; }

  /* Footer */
  .footer { height: 187px; background: var(--footer); color: var(--white); display: flex; padding: 20px 0; }
  .footer-col { flex: 1; padding: 0 28px; }
  .footer-col + .footer-col { border-left: 1px solid var(--divider); }
  .footer-heading { font-size: 19px; font-weight: 600; margin-bottom: 14px; }
  .footer-col.about-col { text-align: center; }
  .footer-copy { font-size: 9px; font-weight: 700; line-height: 2; }
  .footer-links { list-style: none; }
  .footer-links li { font-size: 9px; font-weight: 600; margin-bottom: 12px; }
  .footer-col.touch-col { text-align: center; }
  .touch-form { display: flex; height: 22px; margin: 0 auto 22px; width: 170px; }
  .touch-input { flex: 1; background: var(--white); font-size: 8px; color: var(--muted); padding: 6px; text-align: left; }
  .touch-send { width: 46px; background: var(--green); font-size: 10px; font-weight: 700; display: flex; align-items: center; justify-content: center; }
  .social { display: flex; justify-content: center; gap: 8px; }
  .social span { width: 22px; height: 22px; border-radius: 3px; }
  .social .s1 { background: var(--social-1); }
  .social .s2 { background: var(--social-2); }
  .social .s3 { background: var(--social-3); }
</style>
</head>
<body>
<div class="page">
  <header class="hero">
    <div class="hero-photo" role="img" aria-label="Photo of business people at a desk with a laptop"></div>
    <div class="hero-shade"></div>
    <div class="hero-inner">
      <div class="brand">ClaimVouchly</div>
      <nav class="nav">
        <a class="active" href="#">Home</a>
        <a href="#">Contact Us</a>
        <a href="#">Testimonial</a>
        <a href="#">Terms</a>
      </nav>
      <h1 class="hero-title">Welcome to the Redemption Source</h1>
      <p class="hero-sub">Please enter a valid certificate ID in the form below</p>
      <div class="redeem-form">
        <div class="redeem-input">Enter...</div>
        <div class="redeem-go">GO</div>
      </div>
      <p class="hero-note">To redeem your certificate and to view FAQ's, terms and locations.</p>
    </div>
  </header>

  <section class="about">
    <h2 class="section-title">About</h2>
    <p>JollyPerkHub.com is a leading company in travel certificate fulfillment.</p>
    <p>Our goal is to make it easy for you to redeem your certificate and our philosophy is this: "What good is it to receive a gift certificate if you can't use it?".</p>
    <p>If you have any questions about how to redeem a certain certificate, please contact us. We are here to help.</p>
  </section>

  <section class="testimonials">
    <h2 class="section-title">Testimonials:</h2>
    <p class="quote">"Maren was a "saving grace." She followed up and helped me book the vacation and air fare. Maren was positive and did everything she promised to do. "</p>
    <p class="author">Lena R.</p>
    <div class="arrows">
      <svg width="22" height="22" viewBox="0 0 22 22"><circle cx="11" cy="11" r="10" fill="none" stroke="#1c1c1c" stroke-width="1.5"/><path d="M13 6 L8 11 L13 16" fill="none" stroke="#1c1c1c" stroke-width="1.8"/></svg>
      <svg width="22" height="22" viewBox="0 0 22 22"><circle cx="11" cy="11" r="10" fill="none" stroke="#1c1c1c" stroke-width="1.5"/><path d="M9 6 L14 11 L9 16" fill="none" stroke="#1c1c1c" stroke-width="1.8"/></svg>
    </div>
  </section>

  <section class="newsletter">
    <h2 class="section-title">Get ou newslatter</h2>
    <div class="newsletter-form">
      <div class="newsletter-input">Email...</div>
      <div class="newsletter-send">SEND</div>
    </div>
  </section>

  <footer class="footer">
    <div class="footer-col about-col">
      <h3 class="footer-heading">Logo</h3>
      <p class="footer-copy">Lorem ipsum dolor sit amet,<br>consectetur adipiscing elit,<br>sed do eiusmod tempor</p>
    </div>
    <div class="footer-col">
      <h3 class="footer-heading">Links</h3>
      <ul class="footer-links">
        <li>Home</li>
        <li>Contact Us</li>
        <li>Testimonial</li>
        <li>Terms</li>
      </ul>
    </div>
    <div class="footer-col touch-col">
      <h3 class="footer-heading">Touch Us</h3>
      <div class="touch-form">
        <div class="touch-input">Email...</div>
        <div class="touch-send">SEND</div>
      </div>
      <div class="social"><span class="s1"></span><span class="s2"></span><span class="s3"></span></div>
    </div>
  </footer>
</div>
</body>
</html>
```